Management consultant needs to update look of website

Currently I have a great word press website but it needs an updated look. I have new text for the site in the attached word document. I also have a list of websites whose design, look, and organization i like as a guide for the designer. The final design should be simple, strong, clear, and project the idea that my brand is a powerful authority in this space. Current site = www.brookfernadvisory.com

Target Market(s)

company owners / executives

Industry/Entity Type

Management Consulting

Number of Pages Required

3 page

Font styles to use
Serif

Colors

Designer to choose colors to be used in the design.

Requirements
Must have
• a simple and clear design and message. professional look. easy navigation. responsive to mobile devices. an easily implemented wordpress theme OR squarespace. use of my logo colors. though I am open to changing to a deep navy or charcoal logo image. source file uploaded.
Nice to have
• i like the cover photo and logo watermark on my current homepage. i like the google map with my logo on the current contact page. i like the animation as well. a great blend of the current site and something that is more seamless.

```html
<!DOCTYPE html>
<html lang="en">
<head>
<meta charset="utf-8">
<title>Brookfern Advisory – Strategy, Workshops, Coaching</title>
<link href="https://fonts.googleapis.com/css2?family=Libre+Baskerville:wght@400;700&family=Lato:wght@400;700&display=swap" rel="stylesheet">
<style>
:root{
  --gold:#a8862f;
  --gold-dark:#8c6e22;
  --red:#d7282f;
  --ink:#2b2b2b;
  --text:#555;
  --grey-bg:#f3f3f3;
  --footer:#2f2f2f;
  --line:#d9d9d9;
  --white:#fff;
}
*{box-sizing:border-box;margin:0;padding:0}
html,body{width:1200px;height:4157px;overflow:hidden}
body{font-family:'Lato',sans-serif;color:var(--text);background:var(--white);position:relative}
a{color:inherit;text-decoration:none}

/* header */
.site-header{position:absolute;top:0;left:0;width:1200px;height:180px}
.brand{position:absolute;left:30px;top:6px;width:280px;text-align:center;z-index:2}
.brand-mark{width:80px;height:80px;border-radius:50%;background:var(--gold);margin:0 auto}
.brand-name{font-family:'Libre Baskerville',serif;color:var(--gold);font-size:15px;font-weight:700;margin-top:8px;letter-spacing:.5px;white-space:nowrap}
.brand-tag{font-size:10px;color:var(--gold);letter-spacing:1.2px;margin-top:3px;white-space:nowrap}
.contact-top{position:absolute;top:40px;display:flex;align-items:center;gap:12px}
.contact-top .label{font-size:12px;letter-spacing:1px;color:var(--ink);font-weight:700}
.contact-top .value{font-size:16px;color:var(--ink);font-weight:700;white-space:nowrap}
.contact-top svg{width:30px;height:30px}
.divider-v{position:absolute;left:870px;top:40px;width:2px;height:42px;background:var(--gold)}
.main-nav{position:absolute;top:130px;left:0;width:1200px;height:50px;background:var(--gold)}
.main-nav .brand-plate{position:absolute;left:0;top:0;width:330px;height:50px;background:var(--white);clip-path:polygon(0 0,100% 0,92% 100%,0 100%)}
.main-nav ul{list-style:none;position:absolute;left:330px;top:0;width:870px;height:50px;display:flex}
.main-nav li{font-family:'Libre Baskerville',serif;font-size:13px;color:var(--white);letter-spacing:.8px;height:50px;line-height:50px;flex:1 1 auto;text-align:center;white-space:nowrap;border-right:1px solid rgba(255,255,255,.35)}
.main-nav li.active{background:#5a5a5a;flex:0 0 110px}
.main-nav li:last-child{border-right:0}

/* hero */
.hero{position:absolute;top:180px;left:0;width:1200px;height:580px}
.hero-photo{position:absolute;inset:0;background:linear-gradient(160deg,#6b5a48 0%,#9b7f61 30%,#c7b39b 55%,#8c7259 80%,#4a3d31 100%)}
.hero-badge{position:absolute;left:440px;top:0;width:320px;height:320px;border-radius:50%;background:rgba(40,40,40,.72);display:flex;align-items:center;justify-content:center;text-align:center}
.hero-badge h1{font-family:'Libre Baskerville',serif;color:var(--white);font-size:31px;line-height:1.45;letter-spacing:2px;font-weight:700;margin-top:60px}
.hero-curve{position:absolute;left:0;bottom:0;width:1200px;height:120px}
.hero-dots{position:absolute;left:0;top:548px;width:1200px;display:flex;justify-content:center;gap:8px}
.hero-dots span{width:12px;height:12px;border-radius:50%;border:2px solid #bbb;background:var(--white)}
.hero-dots span.on{background:#bbb}

/* section titles */
.section-title{position:absolute;left:0;width:1200px;text-align:center;font-family:'Libre Baskerville',serif;font-size:36px;color:var(--ink);letter-spacing:1.5px}
.section-title em{font-style:normal;color:var(--red);font-weight:700}
.section-title.gold em{color:var(--gold)}
.title-rule{position:absolute;left:450px;width:300px;height:24px}

/* services */
.service{position:absolute;top:955px;width:335px;height:310px;text-align:center;padding:0 40px}
.service.featured{border:2px solid #e46f73;border-radius:6px}
.service-icon{width:86px;height:86px;border-radius:50%;margin:10px auto 0;display:flex;align-items:center;justify-content:center}
.service-icon.outline{border:2px solid var(--gold)}
.service-icon.filled{background:var(--gold)}
.service h3{font-family:'Libre Baskerville',serif;font-size:16px;color:var(--ink);margin-top:18px;line-height:1.4;letter-spacing:.5px}
.service.featured h3{color:var(--gold)}
.service p{font-size:14px;line-height:1.55;margin-top:12px;color:var(--text)}
.read-more{display:inline-block;font-size:12px;letter-spacing:1px;color:var(--text);border-bottom:1px solid #999;margin-top:14px}

/* about */
.about{position:absolute;top:1365px;left:0;width:1200px;height:535px;background:var(--gold);overflow:hidden}
.about-mark{position:absolute;left:12px;top:40px;width:460px;height:460px;border-radius:50%;background:var(--white)}
.about-body{position:absolute;left:492px;top:95px;width:640px;color:var(--white)}
.about-body h2{font-family:'Libre Baskerville',serif;font-size:29px;font-weight:400;letter-spacing:1px}
.about-body h2 strong{font-weight:700}
.about-body hr{border:0;border-top:1px solid rgba(255,255,255,.45);margin:14px 0 16px}
.about-body p{font-size:14px;line-height:1.6;margin-bottom:12px}
.btn-pill{display:inline-block;background:#5a5a5a;color:var(--white);font-size:14px;letter-spacing:1px;padding:12px 36px;border-radius:30px;margin-top:10px;border:2px solid rgba(255,255,255,.5)}

/* testimonials */
.testimonial{position:absolute;top:2125px;width:320px;text-align:center}
.testimonial .name{font-family:'Libre Baskerville',serif;font-size:16px;color:var(--ink);letter-spacing:1px}
.testimonial .name.hl{color:var(--red)}
.stars{color:var(--gold);font-size:14px;letter-spacing:3px;margin-top:6px}
.quote-card{margin-top:18px;border:1px solid var(--line);border-bottom:3px solid var(--gold);height:112px;padding:18px 20px;text-align:left;font-size:13px;line-height:1.55;color:var(--ink);box-shadow:0 2px 5px rgba(0,0,0,.08);overflow:hidden}
.quote-card .q{color:var(--gold);font-family:'Libre Baskerville',serif;font-weight:700}
.slider-arrow{position:absolute;width:20px;height:34px}

/* blog */
.blog{position:absolute;top:2410px;left:0;width:1200px;height:665px;background:var(--grey-bg)}
.blog-intro{position:absolute;top:178px;left:0;width:1200px;text-align:center;font-size:14px;color:var(--ink)}
.post{position:absolute;top:255px;width:520px;height:340px;background:var(--white);border:1px solid var(--line);border-radius:8px;padding:0 28px}
.post-thumb{position:absolute;left:22px;top:-32px;width:150px;height:150px;border-radius:50%;border:5px solid var(--white);box-shadow:0 1px 4px rgba(0,0,0,.2)}
.post-head{margin-left:160px;padding-top:28px}
.post-head h3{font-family:'Libre Baskerville',serif;color:var(--gold);font-size:15px;line-height:1.35;letter-spacing:.5px}
.post-meta{font-size:13px;color:var(--ink);margin-top:8px;display:flex;gap:22px}
.post p{font-size:14px;line-height:1.6;color:var(--ink);margin-top:22px}

/* clients */
.logo-grid{position:absolute;top:3285px;left:83px;width:1040px;display:grid;grid-template-columns:repeat(5,192px);gap:20px 20px}
.logo-tile{height:86px;border:1px solid #cfcfcf;border-radius:4px;display:flex;align-items:center;justify-content:center;box-shadow:0 1px 3px rgba(0,0,0,.06)}
.logo-tile span{display:block;background:#c9c9c9}
.logo-tile span.r{width:46px;height:46px;border-radius:50%}
.logo-tile span.b{width:120px;height:34px;border-radius:4px}
.logo-tile span.s{width:44px;height:44px;border-radius:4px}

/* footer */
.footer{position:absolute;top:3640px;left:0;width:1200px;height:517px}
.footer-bg{position:absolute;inset:0}
.footer-mark{position:absolute;left:552px;top:8px;width:96px;height:96px;border-radius:50%;background:var(--gold);border:6px solid var(--white);box-shadow:0 0 0 2px var(--gold)}
.footer-col{position:absolute;top:182px;color:#ddd;font-size:14px}
.footer-col h4{font-family:'Libre Baskerville',serif;font-size:14px;color:var(--white);font-weight:400;letter-spacing:1px;margin-bottom:18px}
.footer-col h4 em{font-style:normal;font-weight:700}
.footer-col ul{list-style:none}
.footer-col li{margin-bottom:16px}
.footer-col li::before{content:"›";margin-right:8px;color:#aaa}
.addr{line-height:1.45}
.addr strong{color:var(--white)}
.foot-contact{display:flex;align-items:center;gap:10px;margin-top:26px}
.foot-contact svg{width:16px;height:16px;flex:none}
.inquiry input,.inquiry .msg{display:block;width:250px;height:28px;border:1px solid #aaa;background:transparent;color:#ddd;font-family:'Lato',sans-serif;font-size:12px;padding:0 8px;margin-bottom:6px}
.inquiry .msg{height:48px;padding-top:6px}
.inquiry .submit{display:inline-block;background:#888;color:var(--white);font-size:12px;padding:5px 22px;border-radius:14px;margin-top:4px}
.footer-map{position:absolute;left:888px;top:190px;width:218px;height:218px;border-radius:50%;background:radial-gradient(circle at 40% 40%,#eceae4,#d8d6cf);border:5px solid var(--white)}
.bottom-bar{position:absolute;left:0;bottom:0;width:1200px;height:57px;background:var(--gold);color:var(--white);font-size:13px;display:flex;align-items:center;justify-content:space-between;padding:0 80px}
.socials{display:flex;gap:10px}
.socials span{width:34px;height:34px;border-radius:50%;background:#2d5ea8;border:2px solid var(--white)}
</style>
</head>
<body>

<header class="site-header">
  <nav class="main-nav">
    <div class="brand-plate"></div>
    <ul>
      <li class="active">HOME</li>
      <li>ABOUT US</li>
      <li>OUR SERVICES</li>
      <li>OUR CLIENTS</li>
      <li>CONTACT US</li>
    </ul>
  </nav>
  <div class="brand">
    <div class="brand-mark" role="img" aria-label="Brookfern Advisory emblem"></div>
    <div class="brand-name">BROOKFERN ADVISORY</div>
    <div class="brand-tag">STRATEGY. WORKSHOPS. COACHING</div>
  </div>
  <div class="contact-top" style="left:675px">
    <svg viewBox="0 0 24 24"><path fill="#a8862f" d="M6.6 10.8a15 15 0 0 0 6.6 6.6l2.2-2.2a1 1 0 0 1 1-.25 11.4 11.4 0 0 0 3.6.57 1 1 0 0 1 1 1V20a1 1 0 0 1-1 1A17 17 0 0 1 3 4a1 1 0 0 1 1-1h3.5a1 1 0 0 1 1 1c0 1.25.2 2.450.57 3.57a1 1 0 0 1-.25 1z"/></svg>
    <div><div class="label">CALL US TODAY</div><div class="value">555.014.2290</div></div>
  </div>
  <div class="divider-v"></div>
  <div class="contact-top" style="left:900px">
    <svg viewBox="0 0 24 24"><rect x="2" y="5" width="20" height="14" rx="2" fill="none" stroke="#a8862f" stroke-width="2"/><path d="M2 6l10 7 10-7" fill="none" stroke="#a8862f" stroke-width="2"/></svg>
    <div><div class="label">EMAIL US</div><div class="value">hello@brookfernadvisory.com</div></div>
  </div>
</header>

<section class="hero">
  <div class="hero-photo" role="img" aria-label="Photo of two people at a wooden table with a notebook, glasses and a tablet during a coaching session"></div>
  <div class="hero-badge"><h1>LEADERSHIP<br>TEAM<br>DEVELOPMENT</h1></div>
  <svg class="hero-curve" viewBox="0 0 1200 120" preserveAspectRatio="none">
    <path d="M0 0 Q600 160 1200 0 L1200 120 L0 120 Z" fill="#fff"/>
    <path d="M0 0 Q600 160 1200 0" fill="none" stroke="#a8862f" stroke-width="6"/>
  </svg>
  <div class="hero-dots"><span class="on"></span><span></span><span></span><span></span></div>
</section>

<h2 class="section-title" style="top:842px">OUR <em>SERVICES</em></h2>
<svg class="title-rule" style="top:895px" viewBox="0 0 300 24"><line x1="60" y1="12" x2="132" y2="12" stroke="#a8862f"/><line x1="168" y1="12" x2="240" y2="12" stroke="#a8862f"/><circle cx="150" cy="12" r="9" fill="none" stroke="#a8862f" stroke-width="2"/></svg>

<article class="service" style="left:78px">
  <div class="service-icon outline"><svg width="48" height="48" viewBox="0 0 48 48"><circle cx="24" cy="14" r="6" fill="#a8862f"/><path d="M14 36c0-7 4-11 10-11s10 4 10 11z" fill="#a8862f"/><circle cx="10" cy="20" r="4" fill="#a8862f"/><circle cx="38" cy="20" r="4" fill="#a8862f"/></svg></div>
  <h3>TALENT<br>STRATEGY</h3>
  <p>Business growth, even in the beginning, comes down to hiring the right talent and putting in them in the right position to succeed.</p>
  <a class="read-more">READ MORE »</a>
</article>
<article class="service featured" style="left:430px">
  <div class="service-icon filled"><svg width="48" height="48" viewBox="0 0 48 48"><rect x="10" y="22" width="28" height="6" fill="#fff"/><circle cx="16" cy="15" r="4" fill="#fff"/><circle cx="32" cy="15" r="4" fill="#fff"/><circle cx="24" cy="34" r="4" fill="#fff"/></svg></div>
  <h3>MANAGEMENT<br>WORKSHOPS</h3>
  <p>Bringing an expert in-house to get your leaders on the same page in terms of how to manage, how to lead, and how to show...</p>
  <a class="read-more">READ MORE »</a>
</article>
<article class="service" style="left:787px">
  <div class="service-icon outline"><svg width="48" height="48" viewBox="0 0 48 48"><circle cx="14" cy="20" r="5" fill="#a8862f"/><circle cx="34" cy="20" r="5" fill="#a8862f"/><rect x="8" y="30" width="32" height="4" fill="#a8862f"/><rect x="18" y="6" width="14" height="9" rx="3" fill="none" stroke="#a8862f" stroke-width="2"/></svg></div>
  <h3>EXECUTIVE<br>COACHING</h3>
  <p>I can be incredibly challenging to push yourself, or you company, to the next level without viewing things from...</p>
  <a class="read-more">READ MORE »</a>
</article>

<section class="about">
  <div class="about-mark" role="img" aria-label="Large Brookfern Advisory emblem"></div>
  <div class="about-body">
    <h2>ABOUT <strong>BROOKFERN ADVISORY</strong></h2>
    <hr>
    <p>Dr. Elena Marsh is a business consultant, group trainer, and executive coach specializing in workplace culture, leadership development, and managerial tactics. The founder and director of Brookfern Advisory, she serves as an executive education instructor at Halden University's School of Business.</p>
    <p>Dr. Marsh has earned multiple teaching awards throughout her career thanks to her ability to approach learners from every generation with skill and grace, and she has spent more than 20 years studying the science behind group dynamics, identity, emotion, and the social construction of one's self.</p>
    <a class="btn-pill">READ MORE »</a>
  </div>
</section>

<h2 class="section-title gold" style="top:1988px">CLIENT <em>TESTIMONIALS</em></h2>
<svg class="title-rule" style="top:2042px" viewBox="0 0 300 24"><line x1="60" y1="12" x2="132" y2="12" stroke="#a8862f"/><line x1="168" y1="12" x2="240" y2="12" stroke="#a8862f"/><circle cx="150" cy="12" r="9" fill="none" stroke="#a8862f" stroke-width="2"/></svg>

<svg class="slider-arrow" style="left:38px;top:2222px" viewBox="0 0 20 34"><path d="M16 2L4 17l12 15" fill="none" stroke="#bbb" stroke-width="2"/></svg>
<div class="testimonial" style="left:90px">
  <div class="name hl">MARK T</div><div class="stars">★★★★★</div>
  <div class="quote-card"><span class="q">“</span> Elena Marsh is an outstanding leadership facilitator and professional. I had the opportunity to work with her in facilitating a... <span class="q">[+] ”</span></div>
</div>
<div class="testimonial" style="left:440px">
  <div class="name">SAM RIVERA</div><div class="stars">★★★★★</div>
  <div class="quote-card"><span class="q">“</span> After working in the consulting business for 12 years, I met Elena, I was immediately impressed by her ability to ask the... <span class="q">[+] ”</span></div>
</div>
<div class="testimonial" style="left:790px">
  <div class="name">LENA FORD</div><div class="stars">★★★★★</div>
  <div class="quote-card"><span class="q">“</span> Lorem ipsum dolor sit amet, consectetuer adipiscing elit, sed diam nonummy nibh euismod tincidunt ut laoreet dolore... <span class="q">[+] ”</span></div>
</div>
<svg class="slider-arrow" style="left:1142px;top:2222px" viewBox="0 0 20 34"><path d="M4 2l12 15L4 32" fill="none" stroke="#bbb" stroke-width="2"/></svg>

<section class="blog">
  <h2 class="section-title gold" style="top:85px">RECENT <em>BLOG POSTS</em></h2>
  <svg class="title-rule" style="top:138px" viewBox="0 0 300 24"><line x1="60" y1="12" x2="132" y2="12" stroke="#a8862f"/><line x1="168" y1="12" x2="240" y2="12" stroke="#a8862f"/><circle cx="150" cy="12" r="9" fill="none" stroke="#a8862f" stroke-width="2"/></svg>
  <p class="blog-intro">Brookfern Advisory INSIGHT BLOG will help you gain perspective on yourself, your organization, and how to reach your potential at work.</p>
  <svg class="slider-arrow" style="left:38px;top:405px" viewBox="0 0 20 34"><path d="M16 2L4 17l12 15" fill="none" stroke="#bbb" stroke-width="2"/></svg>
  <article class="post" style="left:82px">
    <div class="post-thumb" role="img" aria-label="Photo of colleagues working at a table in a bright office" style="background:linear-gradient(135deg,#c9c3bd,#8b7a70 60%,#5c5049)"></div>
    <div class="post-head">
      <h3>THE SHOW-UP-ON-<br>TIME RULE</h3>
      <div class="post-meta"><span>September 29, 2017</span><span>▭ (0) Comments</span></div>
    </div>
    <p>recent college grad asked me for advice on how to succeed with a new job. And this was it. To “show-up-on-time.” Likewise, a company owner recently asked me for advice on how to build morale in their office. And this was it. To “show-up-on-time.” It doesn't matter if you are the newest...</p>
    <a class="read-more">READ MORE »</a>
  </article>
  <article class="post" style="left:612px">
    <div class="post-thumb" role="img" aria-label="Photo of a sign reading interview in progress" style="background:linear-gradient(135deg,#a88f6e,#6e5a44 60%,#3f3327)"></div>
    <div class="post-head">
      <h3>HOW TO ASK GREAT INTERVIEW<br>QUESTIONS</h3>
      <div class="post-meta"><span>September 10, 2017</span><span>▭ (0) Comments</span></div>
    </div>
    <p>If you are a manger, you are well aware that hiring the wrong person can destroy a department. Hiring the right person – every time – is the ultimate goal. So how can you ask interview questions that successfully weed out potential bad seeds? Here are 4 strategies to adopt.</p>
    <a class="read-more">READ MORE »</a>
  </article>
  <svg class="slider-arrow" style="left:1142px;top:405px" viewBox="0 0 20 34"><path d="M4 2l12 15L4 32" fill="none" stroke="#bbb" stroke-width="2"/></svg>
</section>

<h2 class="section-title" style="top:3165px">CLIENTS <em>&amp; PARTNERS</em></h2>
<svg class="title-rule" style="top:3218px" viewBox="0 0 300 24"><line x1="60" y1="12" x2="132" y2="12" stroke="#a8862f"/><line x1="168" y1="12" x2="240" y2="12" stroke="#a8862f"/><circle cx="150" cy="12" r="9" fill="none" stroke="#a8862f" stroke-width="2"/></svg>

<div class="logo-grid" aria-label="Client and partner badges">
  <div class="logo-tile"><span class="b"></span></div>
  <div class="logo-tile"><span class="s"></span></div>
  <div class="logo-tile"><span class="b"></span></div>
  <div class="logo-tile"><span class="b"></span></div>
  <div class="logo-tile"><span class="r"></span></div>
  <div class="logo-tile"><span class="r"></span></div>
  <div class="logo-tile"><span class="r"></span></div>
  <div class="logo-tile"><span class="b"></span></div>
  <div class="logo-tile"><span class="b"></span></div>
  <div class="logo-tile"><span class="b"></span></div>
  <div class="logo-tile"><span class="s"></span></div>
  <div class="logo-tile"><span class="b"></span></div>
  <div class="logo-tile"><span class="b"></span></div>
  <div class="logo-tile"><span class="r"></span></div>
  <div class="logo-tile"><span class="b"></span></div>
</div>

<footer class="footer">
  <svg class="footer-bg" viewBox="0 0 1200 517" preserveAspectRatio="none">
    <path d="M0 140 Q600 30 1200 140 L1200 517 L0 517 Z" fill="#2f2f2f"/>
    <path d="M0 140 Q600 30 1200 140" fill="none" stroke="#a8862f" stroke-width="5"/>
  </svg>
  <div class="footer-mark" role="img" aria-label="Brookfern Advisory emblem"></div>

  <div class="footer-col" style="left:80px">
    <h4>QUICK <em>LINKS</em></h4>
    <ul><li>Home</li><li>About Us</li><li>Our Services</li><li>Our Clients</li><li>Contact Us</li></ul>
  </div>
  <div class="footer-col" style="left:258px">
    <h4>CONTACT <em>DETAILS</em></h4>
    <div class="foot-contact" style="margin-top:0;align-items:flex-start">
      <svg viewBox="0 0 24 24"><path fill="#ccc" d="M12 2a7 7 0 0 0-7 7c0 5 7 13 7 13s7-8 7-13a7 7 0 0 0-7-7zm0 9.5A2.5 2.5 0 1 1 12 6.5a2.5 2.5 0 0 1 0 5z"/></svg>
      <div class="addr"><strong>BROOKFERN ADVISORY</strong><br>Riverton Area Chamber of Commerce<br>118 North Elm Street<br>Riverton, GA 30400</div>
    </div>
    <div class="foot-contact"><svg viewBox="0 0 24 24"><path fill="#ccc" d="M6.6 10.8a15 15 0 0 0 6.6 6.6l2.2-2.2a1 1 0 0 1 1-.25 11.4 11.4 0 0 0 3.6.57 1 1 0 0 1 1 1V20a1 1 0 0 1-1 1A17 17 0 0 1 3 4a1 1 0 0 1 1-1h3.5a1 1 0 0 1 1 1c0 1.25.2 2.45.57 3.57a1 1 0 0 1-.25 1z"/></svg>555.014.2290</div>
    <div class="foot-contact"><svg viewBox="0 0 24 24"><rect x="2" y="5" width="20" height="14" rx="2" fill="none" stroke="#ccc" stroke-width="2"/><path d="M2 6l10 7 10-7" fill="none" stroke="#ccc" stroke-width="2"/></svg>hello@brookfernadvisory.com</div>
  </div>
  <div class="footer-col inquiry" style="left:572px">
    <h4>QUICK <em>INQUIRY</em></h4>
    <input type="text" placeholder="Your Name">
    <input type="text" placeholder="Phone">
    <input type="text" placeholder="Email">
    <div class="msg">Message</div>
    <span class="submit">SUBMIT »</span>
  </div>
  <div class="footer-map" role="img" aria-label="Street map showing the office location"></div>

  <div class="bottom-bar">
    <span>Copyright © 2019 Brookfern Advisory, LLC. All Rights Reserved.</span>
    <div class="socials" aria-label="Social links"><span></span><span></span><span></span></div>
  </div>
</footer>

</body>
</html>
```